Home Security Company Business Card

Looking for a eye catching business card that is non traditional and stands out but yet still looks professional. It should include all the pertinent information such as name, title, address, telephone, e-mail, website address should definitely stand out and then finally the logo.

Target Market(s)

Residential and Commercial accounts mostly upscale accounts

Industry/Entity Type

Security

Contact Information for Business Card

Name
Title
Address
Office #
Cell #
E-mail
Website

Font styles to use
Serif
Sans Serif

Requirements
Must have
• Logo, two sided color configuration
Nice to have
• You decide
Should not have
• There really aren't any.

```html
<!DOCTYPE html>
<html lang="en">
<head>
<meta charset="utf-8">
<title>Harborline Protection Group – Business Card</title>
<link rel="stylesheet" href="https://fonts.googleapis.com/css2?family=Tinos:wght@400&family=Mulish:wght@400;700&display=swap">
<style>
  :root {
    --bg: #e9e4dc;
    --paper: #fbfbfa;
    --crimson: #8e1a16;
    --crimson-deep: #6d0f0c;
    --crimson-light: #a63a26;
    --gold: #e2a93b;
    --gold-soft: #f0c766;
    --ink: #5a3a2a;
    --ink-muted: #8a7a70;
  }
  * { box-sizing: border-box; margin: 0; padding: 0; }
  html, body { width: 1200px; height: 1023px; overflow: hidden; }
  body {
    background: var(--bg);
    font-family: "Mulish", Arial, sans-serif;
    position: relative;
  }
  .card {
    position: absolute;
    left: 250px;
    width: 700px;
    height: 400px;
    box-shadow: 0 8px 24px rgba(60, 40, 20, 0.18);
    overflow: hidden;
  }
  .card--front { top: 90px; background: var(--paper); }
  .card--back {
    top: 533px;
    background: radial-gradient(ellipse at 30% 25%, var(--crimson-light) 0%, var(--crimson) 45%, var(--crimson-deep) 100%);
  }

  /* front */
  .band {
    position: absolute;
    left: 120px; top: 0;
    width: 110px; height: 100%;
    background: linear-gradient(90deg, var(--crimson-deep), var(--crimson) 40%, var(--crimson-light) 100%);
    border-left: 4px solid var(--gold);
    border-right: 4px solid var(--gold);
  }
  .band__dot {
    position: absolute;
    left: 50%; top: 64px;
    width: 46px; height: 46px;
    margin-left: -23px;
    border-radius: 50%;
    background: var(--gold);
  }
  .brand {
    position: absolute;
    left: 262px; top: 50px;
    font-family: "Tinos", "Times New Roman", serif;
    color: var(--crimson);
    line-height: 1;
  }
  .brand__name { display: block; font-size: 44px; letter-spacing: 1px; }
  .brand__sub { display: block; font-size: 17px; letter-spacing: 0.5px; margin-top: 4px; }

  .person { position: absolute; left: 262px; top: 180px; }
  .person__name { font-weight: 700; font-size: 19px; color: var(--crimson); }
  .person__title { font-size: 14px; color: var(--gold); margin-top: 2px; }

  .contacts {
    position: absolute;
    left: 262px; top: 250px;
    list-style: none;
    font-size: 15px;
    color: var(--crimson);
  }
  .contacts li { display: flex; align-items: center; gap: 10px; height: 24px; }
  .contacts svg { width: 14px; height: 14px; fill: var(--crimson); flex: none; }

  .address {
    position: absolute;
    left: 530px; top: 180px;
    font-size: 15px;
    line-height: 1.5;
    color: var(--gold);
  }

  /* back */
  .back-brand {
    position: absolute;
    left: 60px; bottom: 60px;
    font-family: "Tinos", "Times New Roman", serif;
    color: #5e0c0a;
    opacity: 0.7;
    line-height: 1;
  }
  .back-brand__name { display: block; font-size: 64px; letter-spacing: 2px; }
  .back-brand__sub { display: block; font-size: 25px; letter-spacing: 1px; margin-top: 6px; }
</style>
</head>
<body>

<section class="card card--front" aria-label="Business card front">
  <div class="band"><span class="band__dot"></span></div>

  <div class="brand">
    <span class="brand__name">HARBORLINE</span>
    <span class="brand__sub">PROTECTION GROUP INC.</span>
  </div>

  <div class="person">
    <p class="person__name">Daniel Reyes</p>
    <p class="person__title">Founder</p>
  </div>

  <ul class="contacts">
    <li>
      <svg viewBox="0 0 14 14" aria-hidden="true"><path d="M1 3h12v8H1z M3 5h8v1H3z"/></svg>
      +698 41 22 60
    </li>
    <li>
      <svg viewBox="0 0 14 14" aria-hidden="true"><path d="M4 0h6a1 1 0 0 1 1 1v12a1 1 0 0 1-1 1H4a1 1 0 0 1-1-1V1a1 1 0 0 1 1-1zm0 2v9h6V2z"/></svg>
      +678 30 57 19
    </li>
    <li>
      <svg viewBox="0 0 14 14" aria-hidden="true"><path d="M0 3h14v8H0zm1 1v.5l6 3.5 6-3.5V4z"/></svg>
      info@harborline.com
    </li>
    <li>
      <svg viewBox="0 0 14 14" aria-hidden="true"><circle cx="7" cy="7" r="6.5"/><path d="M0.5 7h13M7 0.5v13" stroke="#fbfbfa" stroke-width="1"/></svg>
      www.harborline.com
    </li>
  </ul>

  <p class="address">Here your company<br>or home address</p>
</section>

<section class="card card--back" aria-label="Business card back">
  <div class="back-brand">
    <span class="back-brand__name">HARBORLINE</span>
    <span class="back-brand__sub">PROTECTION GROUP INC.</span>
  </div>
</section>

</body>
</html>
```